business card template & company stationery
for Blue Pine Device Wizard - Computer Support
business card template & company stationery -
Creative Brief
Bright & Fun-filled
Dale Harwick
Service Manager
47 E. Birch Ave. (Rt. 58) Ashbury, NH 02519
dale@bluepinedevicewizard.com
www.BluePineDeviceWizard.com
I will upload the logo info shortly. The phone number is the most important contact info for us.
On the back of the card I was planning to have either a solid blue or orange background with our logo centered in all white, but I'm open to other ideas. The white on blue and orange versions are included with the logos

```html
<!DOCTYPE html>
<html lang="en">
<head>
<meta charset="utf-8">
<title>Blue Pine Device Wizard – Business Card</title>
<link href="https://fonts.googleapis.com/css2?family=Source+Sans+3:ital,wght@0,400;0,600;0,700;1,600&display=swap" rel="stylesheet">
<style>
  :root{
    --bg:#e8e5e1;
    --card:#ffffff;
    --brand-blue:#2f77c2;
    --brand-orange:#f47b20;
    --ink:#2c2c2c;
    --icon:#4a6a8c;
    --rule:#c9c9c9;
  }
  html,body{margin:0;padding:0;overflow:hidden;}
  body{
    width:1200px;height:780px;background:var(--bg);
    font-family:"Source Sans 3","Myriad Pro",Arial,sans-serif;
    position:relative;
  }
  .card{
    position:absolute;left:100px;top:104px;width:1000px;height:571px;
    background:var(--card);border-radius:34px;overflow:hidden;
    box-shadow:0 10px 30px rgba(0,0,0,.18);
  }
  .brand{
    position:absolute;left:62px;top:92px;display:flex;align-items:center;gap:22px;
  }
  .brand-dot{width:62px;height:62px;border-radius:50%;background:var(--brand-blue);}
  .brand-name{font-size:52px;font-weight:600;color:var(--brand-orange);letter-spacing:-0.5px;}
  .person{
    position:absolute;left:60px;top:296px;width:300px;text-align:center;
  }
  .person-name{font-size:32px;font-weight:700;color:var(--brand-blue);line-height:1.1;}
  .person-title{font-size:25px;font-weight:600;font-style:italic;color:var(--brand-orange);margin-top:6px;}
  .person-address{font-size:25px;color:var(--ink);line-height:1.3;margin-top:14px;}
  .divider{position:absolute;left:378px;top:290px;width:2px;height:170px;background:var(--rule);}
  .contacts{position:absolute;left:398px;top:292px;margin:0;padding:0;list-style:none;}
  .contacts li{display:flex;align-items:center;gap:14px;height:42px;font-size:24px;color:var(--ink);}
  .contacts svg{width:24px;height:24px;flex:none;}
  .waves{position:absolute;left:0;bottom:0;width:1000px;height:571px;}
</style>
</head>
<body>
  <div class="card">
    <svg class="waves" viewBox="0 0 1000 571" aria-hidden="true">
      <path d="M0,458 C260,560 620,575 1000,440 L1000,571 L0,571 Z" fill="var(--brand-orange)"/>
      <path d="M0,512 C300,590 640,580 1000,462 L1000,571 L0,571 Z" fill="#ffffff"/>
      <path d="M0,522 C300,598 640,588 1000,470 L1000,571 L0,571 Z" fill="var(--brand-blue)"/>
    </svg>

    <div class="brand">
      <span class="brand-dot"></span>
      <span class="brand-name">Blue Pine Device Wizard</span>
    </div>

    <div class="person">
      <div class="person-name">Dale Harwick</div>
      <div class="person-title">Service Manager</div>
      <div class="person-address">47 E. Birch Ave. (Rt. 58)<br>Ashbury, NH 02519</div>
    </div>

    <div class="divider"></div>

    <ul class="contacts">
      <li>
        <svg viewBox="0 0 24 24"><path fill="var(--icon)" d="M6.6 10.8a15.1 15.1 0 0 0 6.6 6.6l2.2-2.2c.3-.3.7-.4 1-.2 1.1.4 2.3.6 3.6.6.6 0 1 .4 1 1V20c0 .6-.4 1-1 1A17 17 0 0 1 3 4c0-.6.4-1 1-1h3.5c.6 0 1 .4 1 1 0 1.3.2 2.5.6 3.6.1.3 0 .7-.2 1z"/></svg>
        (508) 555-0142
      </li>
      <li>
        <svg viewBox="0 0 24 24"><rect x="5" y="9" width="14" height="12" rx="2" fill="var(--icon)"/><path d="M4 8c0-3 16-3 16 0v2h-4V8H8v2H4z" fill="var(--icon)"/><circle cx="12" cy="15" r="2.5" fill="#fff"/></svg>
        (888) 555-0176
      </li>
      <li>
        <svg viewBox="0 0 24 24"><text x="12" y="19" text-anchor="middle" font-size="22" font-weight="700" font-family="Source Sans 3, sans-serif" fill="var(--icon)">@</text></svg>
        dale@bluepinedevicewizard.com
      </li>
      <li>
        <svg viewBox="0 0 24 24"><circle cx="12" cy="12" r="9" fill="none" stroke="var(--icon)" stroke-width="2"/><ellipse cx="12" cy="12" rx="4" ry="9" fill="none" stroke="var(--icon)" stroke-width="1.6"/><path d="M3 12h18" stroke="var(--icon)" stroke-width="1.6"/></svg>
        www.BluePineDeviceWizard.com
      </li>
    </ul>
  </div>
</body>
</html>
```